IT Services Company - Company Logo, Flyer design

We are an IT professional services company that provides technical service and support in the residential market. I would like to create a colorful logo and flyer that will be mainly letterbox dropped.

Target Market(s)

residential

Industry/Entity Type

It Company

Requirements
Must have
• nice look and feel, easy to read

```html
<!DOCTYPE html>
<html lang="en">
<head>
<meta charset="utf-8">
<title>Nexalink Communications – Flyer</title>
<link rel="stylesheet" href="https://fonts.googleapis.com/css2?family=Roboto:wght@400;500;700;900&family=Roboto+Condensed:wght@700&display=swap">
<style>
  :root {
    --blue: #1a9ad9;
    --navy: #0d2740;
    --panel: #14273d;
    --grey: #e4e6e8;
    --text: #1b1f24;
    --page: #eceef0;
    --white: #ffffff;
  }
  * { box-sizing: border-box; margin: 0; padding: 0; }
  html, body { width: 1200px; height: 1200px; overflow: hidden; }
  body {
    background: var(--page);
    font-family: "Roboto", Arial, sans-serif;
    color: var(--text);
    position: relative;
  }
  .flyer {
    position: absolute;
    left: 150px; top: 44px;
    width: 900px; height: 1112px;
    background: var(--white);
    overflow: hidden;
    box-shadow: 0 6px 24px rgba(0,0,0,.18);
  }
  .shapes { position: absolute; inset: 0; width: 900px; height: 1112px; }

  .hero-photo {
    position: absolute; left: 0; top: 34px; width: 545px; height: 400px;
    background: linear-gradient(135deg, #5d6e80 0%, #9aa9b8 45%, #cfd8e1 70%, #7d8e9f 100%);
    clip-path: polygon(0 0, 100% 0, 93% 100%, 0 100%);
  }

  .brand {
    position: absolute; left: 540px; top: 50px;
    display: flex; align-items: center; gap: 10px;
  }
  .brand-dot { width: 44px; height: 44px; border-radius: 50%; background: var(--blue); flex: none; }
  .brand-name {
    font-family: "Roboto Condensed", "Roboto", sans-serif; font-weight: 700;
    color: var(--navy); line-height: 1.05; white-space: nowrap;
  }
  .brand-name .line1 { display: block; font-size: 30px; }
  .brand-name .line2 { display: block; font-size: 15px; }

  .title { position: absolute; right: 28px; top: 150px; text-align: right; white-space: nowrap; }
  .title-main {
    font-family: "Roboto Condensed", "Roboto", sans-serif; font-weight: 700;
    font-size: 50px; line-height: 1; color: var(--blue);
  }
  .title-sub { font-size: 25px; font-weight: 700; color: var(--navy); margin-top: 6px; }
  .established {
    position: absolute; right: 28px; top: 300px;
    font-size: 36px; font-weight: 400; color: var(--text); white-space: nowrap;
  }

  .services {
    position: absolute; left: 36px; top: 450px; width: 392px; height: 525px;
    background: var(--panel); color: var(--white);
    padding: 20px 18px 0 22px;
  }
  .services-intro { font-size: 16.5px; line-height: 1.2; font-weight: 500; color: var(--blue); }
  .services-intro .lead { font-size: 20px; }
  .services-list { list-style: none; margin-top: 18px; }
  .services-list li {
    position: relative; padding-left: 20px;
    font-size: 13.5px; line-height: 1.3; margin-bottom: 7px;
  }
  .services-list li::before {
    content: ""; position: absolute; left: 3px; top: 6px;
    width: 6px; height: 6px; border-radius: 50%; background: var(--blue);
  }

  .rate { position: absolute; left: 505px; top: 482px; width: 380px; }
  .rate-label { font-size: 30px; font-weight: 500; color: var(--blue); line-height: 1.1; }
  .rate-price {
    font-size: 50px; font-weight: 900; color: var(--navy); line-height: 1.05;
    display: flex; align-items: flex-start; gap: 6px; white-space: nowrap;
  }
  .rate-unit { font-size: 19px; font-weight: 500; color: var(--blue); line-height: 1; margin-top: 6px; }
  .rate-note { font-size: 17px; color: var(--text); margin-top: 2px; white-space: nowrap; }

  .quote-box {
    position: absolute; left: 465px; top: 640px; width: 435px; height: 82px;
    background: var(--grey); padding: 16px 16px 0 22px;
    font-size: 20px; font-weight: 500; color: #2d3a47; line-height: 1.25;
  }

  .notes { position: absolute; left: 485px; top: 745px; width: 400px; list-style: none; }
  .notes li {
    position: relative; padding-left: 14px;
    font-size: 13px; line-height: 1.3; color: var(--text); margin-bottom: 5px;
  }
  .notes li::before {
    content: ""; position: absolute; left: 1px; top: 6px;
    width: 5px; height: 5px; border-radius: 50%; background: var(--navy);
  }

  .team-photo {
    position: absolute; left: 472px; top: 860px; width: 400px; height: 222px;
    background: linear-gradient(180deg, #ffffff 0%, #dfe3e8 35%, #2b3442 100%);
  }

  .contact { position: absolute; left: 36px; top: 1000px; font-style: normal; }
  .contact-phone {
    display: flex; align-items: center; gap: 10px; white-space: nowrap;
    font-size: 42px; font-weight: 700; color: var(--navy);
  }
  .contact-web {
    display: flex; align-items: center; gap: 12px; margin-top: 10px;
    font-size: 16px; letter-spacing: 3px; color: var(--text);
  }
  .contact svg { flex: none; }
</style>
</head>
<body>
  <main class="flyer">
    <div class="hero-photo" role="img" aria-label="Businessman in suit holding a smartphone with floating app icons, city skyline behind"></div>

    <svg class="shapes" viewBox="0 0 900 1112" aria-hidden="true">
      <polygon points="300,0 900,0 900,30 290,30" fill="var(--blue)"/>
      <polygon points="490,145 900,145 900,275 465,275" fill="var(--grey)"/>
      <polygon points="520,440 900,388 900,412 540,455" fill="var(--blue)"/>
      <polygon points="0,1092 900,1072 900,1112 0,1112" fill="var(--blue)"/>
    </svg>

    <div class="brand">
      <span class="brand-dot"></span>
      <span class="brand-name">
        <span class="line1">NEXALINK</span>
        <span class="line2">Communications Pty Ltd</span>
      </span>
    </div>

    <header class="title">
      <h1 class="title-main">NEXALINK</h1>
      <p class="title-sub">Communications Pty Ltd</p>
    </header>
    <p class="established">Established 2002</p>

    <section class="services">
      <p class="services-intro"><span class="lead">We are an </span>IT professional services company that provides technical service and support for the North Shore residential market.</p>
      <ul class="services-list">
        <li>Home Network &amp; Wireless setup</li>
        <li>Improvements for extending your home Wireless</li>
        <li>IP Camera installations – external and internal</li>
        <li>Backup solutions either at home or to a cloud provider</li>
        <li>Computer &amp; Network Security</li>
        <li>Email setup</li>
        <li>Domain setup and email migration to cloud</li>
        <li>StreamBox installations and wireless setup<br>Stream movies and shows to your existing TV</li>
        <li>Computer Setup</li>
        <li>New computer recommendations</li>
        <li>New computer unpacking and setup</li>
        <li>Mobile phone setups and training</li>
        <li>Computer training</li>
        <li>Telephony &amp; Network Cable relations and installations</li>
      </ul>
    </section>

    <section class="rate">
      <p class="rate-label">We charge</p>
      <p class="rate-price">$70 Ex GST <span class="rate-unit">per<br>hour</span></p>
      <p class="rate-note">(All major credit cards accepted)</p>
    </section>

    <p class="quote-box">We can procure all new hardware and provide you obligation free quotes.</p>

    <ul class="notes">
      <li>No job is too small, please call or email our team who will be happy to assist with your enquiry and schedule an appointment.</li>
      <li>We can also accommodate afterhours appointments</li>
    </ul>

    <div class="team-photo" role="img" aria-label="Three smiling business people in suits giving thumbs up"></div>

    <address class="contact">
      <p class="contact-phone">
        <svg width="36" height="36" viewBox="0 0 24 24"><path fill="var(--blue)" d="M6.6 10.8a15.1 15.1 0 0 0 6.6 6.6l2.2-2.2a1 1 0 0 1 1-.25 11.4 11.4 0 0 0 3.6.57 1 1 0 0 1 1 1V20a1 1 0 0 1-1 1A17 17 0 0 1 3 4a1 1 0 0 1 1-1h3.5a1 1 0 0 1 1 1c0 1.25.2 2.45.57 3.57a1 1 0 0 1-.25 1z"/></svg>
        55 010 480 920
      </p>
      <p class="contact-web">
        <svg width="20" height="20" viewBox="0 0 24 24"><circle cx="12" cy="12" r="10" fill="var(--blue)"/><path d="M2 12h20M12 2c3 3 3 17 0 20M12 2c-3 3-3 17 0 20" stroke="#fff" stroke-width="1.4" fill="none"/></svg>
        www.nexalinkit.com
      </p>
    </address>
  </main>
</body>
</html>
```